Velvet Lune Fashion Boutigue Website

The Velvet Lune Fashion Boutique is located in Toronto, Canada. We carry high quality, elegant line of clothing including dresses and gowns for women.
Our goal is to help ladies find elegant outfits for any occasions.

I've created the domain - (WorldPress) - http://velvetlune.style/
I need you to:
Design and build my website
Features I need: Home, Visit us (location),About us, Contact us, Book an appointment, Appointment confirmation, Gallery/Products, Events, Links to our social media channels, Sign up for promotions, Collaboration Opportunities for Models, Videos, Size Finder.

I will provide you with images of our collection and a short video, but for the homepage I would like you to utilize elegant, eye-catching and breathtaking images for different pages.

```html
<!DOCTYPE html>
<html lang="en">
<head>
<meta charset="utf-8">
<title>Velvet Lune Fashion Boutique</title>
<link rel="stylesheet" href="https://fonts.googleapis.com/css2?family=Josefin+Sans:wght@300;400;600&family=Open+Sans:wght@400;600;700&display=swap">
<style>
:root{
  --gold:#c08d50;
  --gold-line:#d9b98c;
  --ink:#2b2b2b;
  --text:#555;
  --night:#141414;
  --white:#fff;
}
*{box-sizing:border-box;margin:0;padding:0}
html,body{width:1200px;height:2908px;overflow:hidden}
body{position:relative;background:var(--white);font-family:"Open Sans",Arial,sans-serif;color:var(--text)}
.abs{position:absolute}

/* hero */
.hero{top:0;left:0;width:1200px;height:650px;overflow:hidden}
.hero-photo{position:absolute;inset:0;background:
  radial-gradient(ellipse 700px 260px at 620px 560px,#e3262b 0%,#b10f14 55%,transparent 80%),
  linear-gradient(180deg,#3b4248 0%,#5c6369 30%,#2e3337 55%,#8e1014 62%,#c3141a 80%,#9a0d12 100%)}
.brand{left:97px;top:40px;width:260px;text-align:center;color:var(--white)}
.brand-mark{display:block;width:22px;height:22px;border-radius:50%;background:var(--white);margin:0 auto 42px}
.brand-name{font-family:"Josefin Sans",Arial,sans-serif;font-size:40px;font-weight:300;letter-spacing:3px;line-height:1;white-space:nowrap}
.topline{right:98px;top:38px;color:var(--white);font-family:"Josefin Sans",Arial,sans-serif;font-size:15px;display:flex;align-items:center;gap:10px}
.topline svg{fill:var(--gold)}
.topline .sep{margin:0 10px}
.nav{right:90px;top:86px;display:flex;gap:22px;font-family:"Josefin Sans",Arial,sans-serif;font-size:15px;color:var(--white);align-items:center;white-space:nowrap}
.nav .active{color:var(--gold)}
.hero-band{left:0;top:384px;width:1200px;height:116px;background:rgba(90,8,10,.55);display:flex;align-items:center;justify-content:center}
.hero-title{font-family:"Josefin Sans",Arial,sans-serif;font-weight:400;font-size:66px;letter-spacing:9px;color:var(--white);padding-top:8px}
.dots{top:588px;left:568px;display:flex;gap:4px}
.dots span{width:14px;height:14px;border-radius:50%;border:2px solid var(--white)}
.dots span.on{background:var(--white)}

/* welcome */
.welcome-frame{left:99px;top:758px;width:1002px;height:386px;border:1px solid var(--gold-line)}
.welcome-mark{left:588px;top:735px;width:24px;height:24px;border-radius:50%;background:var(--gold)}
.section-title{font-family:"Josefin Sans",Arial,sans-serif;font-weight:400;color:var(--ink);text-transform:uppercase;text-align:center}
.welcome-title{left:0;top:850px;width:1200px;font-size:44px}
.welcome-copy{left:180px;top:924px;width:840px;font-size:14.5px;line-height:31px;text-align:center}
.btn{display:flex;align-items:center;justify-content:center;font-family:"Open Sans",Arial,sans-serif;font-weight:700;font-size:16px;color:var(--white);text-transform:uppercase;background:var(--gold)}
.welcome-btn{left:520px;top:1116px;width:161px;height:55px}

/* collaboration */
.collab-photo{left:0;top:1275px;width:458px;height:525px;background:linear-gradient(100deg,#e6d6cb 0%,#f4ece7 40%,#d9c2b6 70%,#efe5df 100%)}
.collab-panel{left:458px;top:1275px;width:742px;height:525px;background:var(--gold)}
.collab-title{left:508px;top:1350px;width:660px;font-family:"Josefin Sans",Arial,sans-serif;font-weight:300;font-size:44px;line-height:60px;color:var(--white);text-transform:uppercase}
.collab-copy{left:510px;top:1494px;width:590px;font-size:14.5px;line-height:29px;color:var(--white)}
.collab-btn{left:510px;top:1655px;width:260px;height:60px;border:2px solid var(--white);background:transparent}

/* promotions */
.promo-title{left:0;top:1885px;width:1200px;font-size:44px}
.promo-copy{left:180px;top:1953px;width:840px;font-size:14.5px;line-height:31px;text-align:center}
.promo-btn{left:519px;top:2050px;width:163px;height:64px}

/* contact */
.contact{left:0;top:2205px;width:1200px;height:703px}
.contact-title{left:0;top:2350px;width:1200px;font-size:44px;color:var(--white);font-weight:400}
.col-title{font-family:"Open Sans",Arial,sans-serif;font-weight:600;font-size:15px;color:var(--white);text-transform:uppercase}
.form-title{left:99px;top:2438px}
.label{left:99px;font-size:11px;color:var(--white);text-transform:uppercase}
.field{left:99px;width:629px;background:var(--white);border:1px solid #999}
.submit{left:643px;top:2737px;width:87px;height:39px;font-size:14px}
.info-title{left:808px;top:2438px}
.info-row{left:808px;display:flex;gap:18px;align-items:flex-start;color:var(--white);font-size:14.5px;line-height:25px}
.info-icon{width:38px;height:38px;border-radius:50%;border:1px solid #666;display:flex;align-items:center;justify-content:center;flex:none}
.info-icon svg{fill:var(--gold)}
.footer-rule{left:99px;top:2823px;width:1002px;height:1px;background:#3a3a3a}
.copyright{left:99px;top:2852px;font-size:12px;color:var(--white)}
.social{left:916px;top:2843px;display:flex;gap:8px}
.social span{width:30px;height:30px;border-radius:50%;border:1.5px solid var(--white)}
</style>
</head>
<body>

<section class="abs hero">
  <div class="hero-photo" role="img" aria-label="Woman in a flowing red silk gown seen from behind against a dark grey backdrop"></div>
  <div class="abs brand">
    <span class="brand-mark"></span>
    <div class="brand-name">VELVET LUNE</div>
  </div>
  <div class="abs topline">
    <svg width="14" height="14" viewBox="0 0 24 24"><path d="M6.6 10.8a15 15 0 0 0 6.6 6.6l2.2-2.2c.3-.3.7-.4 1-.2 1.1.4 2.3.6 3.6.6.6 0 1 .4 1 1V20c0 .6-.4 1-1 1A17 17 0 0 1 3 4c0-.6.4-1 1-1h3.5c.6 0 1 .4 1 1 0 1.3.2 2.5.6 3.6.1.3 0 .7-.2 1z"/></svg>
    <span>647-555-0182</span>
    <span class="sep">|</span>
    <svg width="16" height="13" viewBox="0 0 24 18"><path d="M0 0h24v2L12 10 0 2z M0 4.5l12 8 12-8V18H0z"/></svg>
    <span>Mira.L@Velvetlune.Style</span>
  </div>
  <nav class="abs nav">
    <span class="active">Home</span><span>Book an appointment</span><span>Visit us</span><span>Gallery/Products</span><span>Events</span><span>About us</span><span>Contact us</span>
    <svg width="15" height="15" viewBox="0 0 24 24"><circle cx="10" cy="10" r="7" fill="none" stroke="#fff" stroke-width="3"/><path d="M15 15l7 7" stroke="#fff" stroke-width="3.5"/></svg>
  </nav>
  <div class="abs hero-band"><h1 class="hero-title">FASHION BOUTIQUE</h1></div>
  <div class="abs dots"><span class="on"></span><span></span><span></span><span></span></div>
</section>

<section>
  <div class="abs welcome-frame"></div>
  <div class="abs welcome-mark"></div>
  <h2 class="abs section-title welcome-title">Welcome to Velvet Lune</h2>
  <p class="abs welcome-copy">Nam libero tempore, cum soluta nobis est eligendi optio cumque nihil impedit quo minus id quod maxime placeat facere possimus, omnis voluptas assumenda est, omnis dolor repellendus. Temporibus autem quibusdam et aut officiis debitis aut rerum necessitatibus saepe eveniet ut et voluptates repudiandae sint et molestiaemo enim ipsam voluptatem quia voluptas sit aspernatur aut odit aut fugit, sed quia consequuntur magni dolores eos qui ratione voluptatem sequi nesciunt. Neque porro quisquam est, qui dolorem ipsum quia dolor sit amet, consectetur, adipisci veli.</p>
  <div class="abs btn welcome-btn">Read more</div>
</section>

<section>
  <div class="abs collab-photo" role="img" aria-label="Model in a white lace top and blush skirt leaning against a pale wooden wall"></div>
  <div class="abs collab-panel"></div>
  <h2 class="abs collab-title">Collaboration opportunities for models</h2>
  <p class="abs collab-copy">Lorem ipsum dolor sit amet, consectetur adipiscing elit, sed do eiusmod tempor incidie dunt ut labore et dolore magna aliqua. Ut enim ad minim veniam, quis nostrud exercit ation ullamco laboris nisi ut aliquip ex ea commodo consequat. Duis aute irure dolor in reprehenderit in voluptate velit esse cillum dolore.</p>
  <div class="abs btn collab-btn">Find an opportunity</div>
</section>

<section>
  <h2 class="abs section-title promo-title">Sign up for promotions</h2>
  <p class="abs promo-copy">Nam libero tempore, cum soluta nobis est eligendi optio cumque nihil impedit quo minus id quod maxime placeat facere possimus, omnis voluptas assumenda est, omnis dolor repellendus. Temporibus autem quibusdam et aut</p>
  <div class="abs btn promo-btn">Sign up</div>
</section>

<section>
  <svg class="abs contact" viewBox="0 0 1200 703" aria-hidden="true">
    <polygon points="0,230 555,0 645,0 1200,230 1200,703 0,703" fill="#141414"/>
    <polyline points="0,262 572,30 628,30 1200,262" fill="none" stroke="#fff" stroke-width="3"/>
  </svg>
  <h2 class="abs section-title contact-title">Contact</h2>

  <div class="abs col-title form-title">Contact form</div>
  <div class="abs label" style="top:2480px">Name :</div>
  <div class="abs field" style="top:2509px;height:33px"></div>
  <div class="abs label" style="top:2550px">Email :</div>
  <div class="abs field" style="top:2576px;height:33px"></div>
  <div class="abs label" style="top:2617px">Message :</div>
  <div class="abs field" style="top:2643px;height:80px"></div>
  <div class="abs btn submit">Submit</div>

  <div class="abs col-title info-title">Contact information</div>
  <div class="abs info-row" style="top:2490px">
    <span class="info-icon"><svg width="12" height="16" viewBox="0 0 24 32"><path d="M12 0a12 12 0 0 0-12 12c0 9 12 20 12 20s12-11 12-20A12 12 0 0 0 12 0zm0 17a5 5 0 1 1 0-10 5 5 0 0 1 0 10z"/></svg></span>
    <span>Lakeshore Studio Suites<br>48 Maple Crest Rd, Scarborough,<br>ON M1T 3K2, Canada</span>
  </div>
  <div class="abs info-row" style="top:2590px">
    <span class="info-icon"><svg width="14" height="14" viewBox="0 0 24 24"><path d="M6.6 10.8a15 15 0 0 0 6.6 6.6l2.2-2.2c.3-.3.7-.4 1-.2 1.1.4 2.3.6 3.6.6.6 0 1 .4 1 1V20c0 .6-.4 1-1 1A17 17 0 0 1 3 4c0-.6.4-1 1-1h3.5c.6 0 1 .4 1 1 0 1.3.2 2.5.6 3.6.1.3 0 .7-.2 1z"/></svg></span>
    <span style="padding-top:6px">647-555-0182</span>
  </div>
  <div class="abs info-row" style="top:2666px">
    <span class="info-icon"><svg width="14" height="11" viewBox="0 0 24 18"><path d="M0 0h24v2L12 10 0 2z M0 4.5l12 8 12-8V18H0z"/></svg></span>
    <span style="padding-top:6px">Mira.L@Velvetlune.Style</span>
  </div>

  <div class="abs footer-rule"></div>
  <div class="abs copyright">Copyrights © 2018, Velvet Lune. All Rights Reserved.</div>
  <div class="abs social"><span></span><span></span><span></span><span></span><span></span></div>
</section>

</body>
</html>
```